Halvering Family Dentistry
Peter K. Wadlow, DDS
Project: Halvering Family Dentistry
Halvering Family Dentistry -
Creative Brief
Professional
7182 Quillan Road, Unit C Charlottesville, VA 40317
smyle7q@postvale.net

```html
<!DOCTYPE html>
<html lang="en">
<head>
<meta charset="utf-8">
<title>Halvering Family Dentistry – Stationery Set</title>
<link rel="stylesheet" href="https://fonts.googleapis.com/css2?family=Libre+Baskerville:wght@700&family=Open+Sans:wght@400;600&display=swap">
<style>
  :root {
    --green: #1f8a4c;
    --ink: #1e1e1e;
    --grey: #7a7a7a;
    --rule: #b9b9b9;
    --paper: #ffffff;
    --bg: #ffffff;
    --shadow: rgba(0,0,0,0.22);
  }
  * { box-sizing: border-box; margin: 0; padding: 0; }
  html, body { width: 1200px; height: 482px; overflow: hidden; background: var(--bg); }
  body { position: relative; font-family: "Open Sans", Arial, sans-serif; color: var(--ink); }

  .sheet {
    position: absolute;
    background: var(--paper);
    box-shadow: 1px 2px 5px var(--shadow);
    overflow: hidden;
  }

  .brand { font-family: "Libre Baskerville", Georgia, serif; font-weight: 700; color: var(--green); line-height: 1; }
  .brand .name { display: block; letter-spacing: 0.02em; }
  .brand .sub { display: block; letter-spacing: 0.12em; margin-top: 2px; }
  .tagline { font-family: "Open Sans", Arial, sans-serif; font-weight: 400; font-size: 4px; letter-spacing: 0.1em; color: var(--grey); text-transform: uppercase; margin-top: 3px; }

  /* Footer band: one thick green rule over one thin dark rule */
  .band { position: absolute; left: 0; width: 100%; }
  .band::before, .band::after { content: ""; display: block; width: 100%; }
  .band::before { height: 3px; background: var(--green); }
  .band::after { height: 1px; background: var(--ink); margin-top: 3px; }

  .address { position: absolute; left: 0; width: 100%; text-align: center; font-size: 5px; color: var(--ink); line-height: 1.5; }

  /* Fax sheet */
  .fax { left: 19px; top: 19px; width: 305px; height: 394px; }
  .fax .brand { position: absolute; top: 16px; left: 0; width: 100%; text-align: center; }
  .fax .brand .name { font-size: 13px; }
  .fax .brand .sub { font-size: 4.8px; }
  .fax-fields { position: absolute; top: 118px; left: 30px; right: 30px; display: grid; grid-template-columns: 1fr 1fr; column-gap: 18px; row-gap: 13px; }
  .field { display: flex; align-items: flex-end; font-size: 5px; }
  .field span { width: 26px; }
  .field i { flex: 1; border-bottom: 0.6px solid var(--rule); height: 6px; }
  .fax-checks { position: absolute; top: 232px; left: 30px; right: 30px; display: flex; justify-content: space-between; font-size: 4.6px; }
  .fax-checks label::before { content: ""; display: inline-block; width: 4px; height: 4px; border: 0.6px solid var(--ink); margin-right: 2px; vertical-align: -0.5px; }
  .fax .band { top: 348px; }
  .fax .address { top: 368px; }

  /* Envelope */
  .envelope-front { left: 365px; top: 62px; width: 350px; height: 152px; }
  .envelope-front .brand { position: absolute; left: 14px; top: 12px; }
  .envelope-front .brand .name { font-size: 10px; }
  .envelope-front .brand .sub { font-size: 3.8px; }
  .envelope-front .return { position: absolute; left: 0; top: 72px; width: 100%; text-align: center; font-size: 4.2px; line-height: 1.6; }
  .envelope-front .band { top: 104px; }

  .envelope-back { left: 365px; top: 252px; width: 350px; height: 150px; }
  .envelope-back svg.flap { position: absolute; inset: 0; width: 100%; height: 100%; }
  .envelope-back .seal { position: absolute; left: 0; width: 100%; top: 46px; text-align: center; }
  .envelope-back .seal .name { font-size: 6px; }

  /* Letterhead */
  .letterhead { left: 770px; top: 19px; width: 240px; height: 390px; }
  .letterhead .brand { position: absolute; top: 16px; right: 20px; }
  .letterhead .brand .name { font-size: 11px; }
  .letterhead .brand .sub { font-size: 4px; }
  .letterhead .band { top: 346px; }
  .letterhead .address { top: 364px; }

  /* Business cards */
  .card-front { left: 1032px; top: 66px; width: 140px; height: 78px; }
  .card-front .contact { position: absolute; left: 8px; top: 8px; border: 0.6px solid var(--rule); padding: 3px 4px; font-size: 3.6px; line-height: 1.5; }
  .card-front .contact strong { font-weight: 600; color: var(--green); font-size: 4px; }
  .card-front .brand { position: absolute; right: 8px; top: 40px; }
  .card-front .brand .name { font-size: 7px; }
  .card-front .brand .sub { font-size: 2.6px; }
  .card-front .band { top: 62px; }

  .card-back { left: 1032px; top: 178px; width: 140px; height: 78px; }
  .card-back .brand { position: absolute; left: 0; width: 100%; top: 28px; text-align: center; }
  .card-back .brand .name { font-size: 6px; }
  .card-back .band { top: 62px; }
</style>
</head>
<body>

<section class="sheet fax">
  <div class="brand"><span class="name">HALVERING</span><span class="sub">FAMILY DENTISTRY</span><div class="tagline">Gentle care for the whole family</div></div>
  <div class="fax-fields">
    <div class="field"><span>To:</span><i></i></div>
    <div class="field"><span>From:</span><i></i></div>
    <div class="field"><span>Fax:</span><i></i></div>
    <div class="field"><span>Pages:</span><i></i></div>
    <div class="field"><span>Phone:</span><i></i></div>
    <div class="field"><span>Date:</span><i></i></div>
    <div class="field"><span>Re:</span><i></i></div>
    <div class="field"><span>CC:</span><i></i></div>
  </div>
  <div class="fax-checks">
    <label>Urgent</label><label>For Review</label><label>Please Comment</label><label>Please Reply</label><label>Please Recycle</label>
  </div>
  <div class="band"></div>
  <p class="address">7182 Quillan Road, Unit C | Charlottesville, VA 40317<br>smyle7q@postvale.net</p>
</section>

<section class="sheet envelope-front">
  <div class="brand"><span class="name">HALVERING</span><span class="sub">FAMILY DENTISTRY</span><div class="tagline">Gentle care for the whole family</div></div>
  <p class="return">7182 Quillan Road, Unit C | Charlottesville, VA 40317<br>Phone: 434.555.0182 | smyle7q@postvale.net</p>
  <div class="band"></div>
</section>

<section class="sheet envelope-back">
  <svg class="flap" viewBox="0 0 350 150" preserveAspectRatio="none">
    <path d="M0 0 L175 86 L350 0" fill="none" stroke="var(--rule)" stroke-width="0.8"/>
  </svg>
  <div class="seal brand"><span class="name">HALVERING</span></div>
</section>

<section class="sheet letterhead">
  <div class="brand"><span class="name">HALVERING</span><span class="sub">FAMILY DENTISTRY</span><div class="tagline">Gentle care for the whole family</div></div>
  <div class="band"></div>
  <p class="address">7182 Quillan Road, Unit C | Charlottesville, VA 40317<br>smyle7q@postvale.net</p>
</section>

<section class="sheet card-front">
  <div class="contact"><strong>Peter K. Wadlow, DDS</strong><br>7182 Quillan Road, Unit C<br>Charlottesville, VA 40317<br>smyle7q@postvale.net</div>
  <div class="brand"><span class="name">HALVERING</span><span class="sub">FAMILY DENTISTRY</span></div>
  <div class="band"></div>
</section>

<section class="sheet card-back">
  <div class="brand"><span class="name">HALVERING</span></div>
  <div class="band"></div>
</section>

</body>
</html>
```